The Crest Company Sweet Packaging Design

The Saffire Crest Company is looking for a logo and label design for an upcoming line of honey based health and beauty products that are sourced from the Polynesian Islands (Hawaii, New Zealand, Fiji etc.).The brand will be premium price positioned and the design and packaging should exude class and quality.The design should be flexible enough to add products from future locations.We would like to see the design across three different product forms:1. Glass Honey Jar (main product)2. Hand cream / lotion (pump bottle, or lotion tube)3. Small box (e.g. throat lozenges / gum packet etc.)The Polynesia Islands are unique and exotic locations; the design/packaging should reflect this but should not be overly complicated. Each individual island has their own distinct culture and history but they have many commonalities which fall under "Polynesian Culture". The Saffire Crest Company is an umbrella brand that should be able to support a growing number of products.Possible designs may (but are not required to) incorporate local flowers (Hawaii / Hibiscus flower, New Zealand / Manuka Flower etc.) into the design, Islands, and boutique feel (elegant classy looking)Please feel free to ask more questions for further guidance but we really want to see where the creative process can take us outside of what we have already considered internally.
Updates

We needed to modify our idea slightly because of competition.

We needed extend to get a few more ideas. We did not want to copy our competition and needed to add a part to our design that we did not include before.

Target Market(s)

Health conscious people. Honey lovers.

Font styles to use
Serif
Sans Serif
Decorative

Colors

Designer to choose colors to be used in the design.

Requirements
Must have
• a little tribal look. because its 100% polynesian Honey.. it would be nice to have the fee of that in the design..

```html
<!DOCTYPE html>
<html lang="en">
<head>
<meta charset="utf-8">
<title>The Saffire Crest Company – Polynesian Honey Label</title>
<link href="https://fonts.googleapis.com/css2?family=Crimson+Text:wght@400;600;700&display=swap" rel="stylesheet">
<style>
  :root {
    --backdrop: #2a2a2a;
    --label-white: #ffffff;
    --ink: #1c1c1c;
    --gold-light: #f3d9a4;
    --gold-mid: #d9a85a;
    --gold-deep: #8a4a12;
    --line-grey: #9a9a9a;
    --bee-yellow: #f2c230;
    --flower-grey: #e6e6e6;
  }
  * { margin: 0; padding: 0; box-sizing: border-box; }
  html, body {
    width: 1200px; height: 1067px; overflow: hidden;
    background: var(--backdrop);
    font-family: "Crimson Text", Georgia, serif;
  }
  .label {
    position: absolute; left: 397px; top: 328px;
    width: 407px; height: 508px;
    background: var(--label-white);
    color: var(--ink);
  }
  .gold-band {
    position: absolute; left: 0; width: 100%; height: 14px;
    background: linear-gradient(90deg, var(--gold-light) 0%, var(--gold-mid) 8%, var(--label-white) 9%, var(--label-white) 11%, var(--gold-light) 12%, var(--gold-mid) 40%, var(--gold-deep) 55%, var(--gold-mid) 70%, var(--gold-light) 88%, var(--label-white) 89%, var(--label-white) 91%, var(--gold-mid) 92%, var(--gold-light) 100%);
  }
  .gold-band--top { top: 14px; }
  .gold-band--bottom { top: 481px; }
  .flower-art {
    position: absolute; left: 262px; top: 342px; width: 125px; height: 130px;
    border-radius: 45% 55% 40% 60%;
    background: radial-gradient(circle at 50% 45%, var(--flower-grey) 0%, #f3f3f3 55%, var(--label-white) 80%);
    z-index: 0;
  }
  .flight-path { position: absolute; left: 0; top: 0; z-index: 1; }
  .bee-art {
    position: absolute; width: 55px; height: 48px; border-radius: 50%;
    background: radial-gradient(circle at 50% 55%, var(--bee-yellow) 0%, #e9e1c4 55%, var(--label-white) 75%);
    z-index: 2;
  }
  .bee-art--left { left: 72px; top: 54px; }
  .bee-art--right { left: 280px; top: 54px; }
  .brand-mark {
    position: absolute; left: 0; top: 48px; width: 100%;
    display: flex; flex-direction: column; align-items: center; gap: 6px;
    z-index: 2;
  }
  .brand-mark__circle {
    width: 64px; height: 64px; border-radius: 50%;
    border: 3px solid var(--ink);
  }
  .brand-mark__name { font-size: 14px; font-weight: 600; letter-spacing: 0.3px; line-height: 1; }
  .text-line { position: absolute; left: 0; width: 100%; text-align: center; line-height: 1; z-index: 2; }
  .headline-pure { top: 170px; font-size: 37px; font-weight: 700; }
  .headline-region { top: 215px; font-size: 53px; font-weight: 600; letter-spacing: 1px; }
  .headline-product { top: 283px; font-size: 53px; font-weight: 700; }
  .rule {
    position: absolute; left: 115px; width: 175px; height: 3px; z-index: 2;
    background: linear-gradient(90deg, var(--gold-light), var(--gold-mid) 30%, var(--gold-deep) 55%, var(--gold-mid) 80%, var(--gold-light));
  }
  .rule--upper { top: 349px; }
  .rule--lower { top: 393px; }
  .variety { top: 360px; font-size: 23px; font-weight: 600; }
  .net-weight { top: 447px; font-size: 16px; font-weight: 600; }
</style>
</head>
<body>
  <div class="label">
    <div class="gold-band gold-band--top"></div>

    <div class="flower-art" role="img" aria-label="Line drawing of tropical blossoms"></div>

    <svg class="flight-path" width="407" height="508" viewBox="0 0 407 508" aria-hidden="true">
      <path d="M98 82 C50 120 30 200 40 280 C52 360 130 405 260 405" fill="none" stroke="var(--line-grey)" stroke-width="1.2" stroke-dasharray="4 3"/>
      <path d="M310 82 C360 120 385 200 375 280 C370 320 355 340 340 350" fill="none" stroke="var(--line-grey)" stroke-width="1.2" stroke-dasharray="4 3"/>
    </svg>

    <div class="bee-art bee-art--left" role="img" aria-label="Illustrated honey bee flying"></div>
    <div class="bee-art bee-art--right" role="img" aria-label="Illustrated honey bee flying"></div>

    <div class="brand-mark">
      <div class="brand-mark__circle"></div>
      <div class="brand-mark__name">The Saffire Crest Company</div>
    </div>

    <div class="text-line headline-pure">100% Pure</div>
    <div class="text-line headline-region">Polynesian</div>
    <div class="text-line headline-product">Honey</div>

    <div class="rule rule--upper"></div>
    <div class="text-line variety">Tropical Honey</div>
    <div class="rule rule--lower"></div>

    <div class="text-line net-weight">Net Weight 1kg (2.2046 lbs)</div>

    <div class="gold-band gold-band--bottom"></div>
  </div>
</body>
</html>
```